Upgrade Brenmoors

Hi,
We are an accounting firm looking to upgrade the following:
Logo, letterhead, withcomp slips and maybe our business cards. I have attached our original letterhead (sample A) and a letterhead (SAmple B) which we like the design and layout, however I want to stick with the colours of our orginal letterhead (Sample A) but improve and modernise the look with other letter head (Sample B) I have attached both. On the footer of Sample A, we would like to remove the names of the directors but leave EST. 1985 we also want to add the MDV logo ABN and TAX AGENT logo as stated in Sample B , we would like to do a layout for the header similar to SAmple B however maybe a bit more structured.

```html
<!DOCTYPE html>
<html lang="en">
<head>
<meta charset="utf-8">
<title>Brenmoors Accountants – Letterhead</title>
<link href="https://fonts.googleapis.com/css2?family=Roboto:wght@700&family=Roboto+Condensed:wght@700&display=swap" rel="stylesheet">
<style>
  :root {
    --navy: #123a73;
    --ink: #111111;
    --accent: #e07028;
    --badge-green: #a6c63c;
    --paper: #ffffff;
  }
  html, body {
    margin: 0;
    padding: 0;
    width: 849px;
    height: 1200px;
    overflow: hidden;
    background: var(--paper);
  }
  .letterhead {
    position: relative;
    width: 849px;
    height: 1200px;
    background: var(--paper);
    font-family: "Roboto", Arial, sans-serif;
    font-weight: 700;
    color: var(--ink);
  }
  .brand-name {
    position: absolute;
    left: 52px;
    top: 42px;
    font-size: 35px;
    line-height: 1;
    letter-spacing: -0.4px;
    color: var(--navy);
  }
  .brand-sub {
    position: absolute;
    left: 60px;
    top: 87px;
    display: flex;
    align-items: center;
    gap: 10px;
    font-size: 22px;
    line-height: 1;
    color: var(--ink);
  }
  .brand-mark {
    width: 13px;
    height: 13px;
    background: var(--navy);
  }
  .contact-item {
    position: absolute;
    display: flex;
    align-items: center;
    gap: 5px;
    font-size: 11.2px;
    line-height: 1;
    white-space: nowrap;
  }
  .contact-item svg { flex: none; }
  .address { left: 322px; top: 52px; }
  .postal  { left: 560px; top: 52px; gap: 7px; }
  .phone   { left: 296px; top: 78px; gap: 8px; }
  .email   { left: 418px; top: 78px; }
  .web     { left: 572px; top: 78px; gap: 6px; }

  .est {
    position: absolute;
    left: 361px;
    top: 1090px;
    font-size: 12.5px;
    line-height: 1;
  }
  .member-badge {
    position: absolute;
    left: 540px;
    top: 1031px;
    width: 46px;
    height: 46px;
    border-radius: 50%;
    background: var(--accent);
  }
  .registration-badge {
    position: absolute;
    left: 670px;
    top: 1032px;
    width: 74px;
    height: 74px;
    border-radius: 50%;
    border: 1px solid var(--ink);
    box-sizing: border-box;
    display: flex;
    align-items: center;
    justify-content: center;
  }
  .registration-badge::after {
    content: "";
    width: 46px;
    height: 46px;
    border-radius: 50%;
    background: var(--badge-green);
  }
  .tax-agent {
    position: absolute;
    left: 751px;
    top: 1054px;
    font-family: "Roboto Condensed", "Arial Narrow", sans-serif;
    font-size: 7.6px;
    line-height: 12px;
  }
</style>
</head>
<body>
<div class="letterhead">
  <header>
    <div class="brand-name">Brenmoors</div>
    <div class="brand-sub">
      <span class="brand-mark"></span>
      <span>Accountants</span>
    </div>

    <div class="contact-item address">
      <svg width="11" height="17" viewBox="0 0 11 17" aria-hidden="true">
        <path d="M5.5 0.5A5 5 0 0 0 0.5 5.5c0 3.6 5 11 5 11s5-7.4 5-11a5 5 0 0 0-5-5z" fill="var(--accent)"/>
        <circle cx="5.5" cy="5.3" r="2" fill="#fff"/>
      </svg>
      <span>ABN 41 502 736 918,742 Linden Street</span>
    </div>
    <div class="contact-item postal">
      <svg width="16" height="12" viewBox="0 0 16 12" aria-hidden="true">
        <rect x="0.6" y="0.6" width="14.8" height="10.8" fill="none" stroke="var(--accent)" stroke-width="1.2"/>
        <path d="M0.6 0.6L8 7l7.4-6.4M0.6 11.4l5.4-5.6M15.4 11.4L10 5.8" fill="none" stroke="var(--accent)" stroke-width="1.1"/>
      </svg>
      <span>PO BOX 318. Ashbury Vic 3190</span>
    </div>

    <div class="contact-item phone">
      <svg width="17" height="16" viewBox="0 0 17 16" aria-hidden="true">
        <path d="M3 1.5l2.2-.8 1.8 3.5-1.5 1.2c.8 2 2.3 3.6 4.2 4.6l1.3-1.4 3.3 2-.7 2.3c-.4 1-1.6 1.6-2.7 1.2C6.4 12.7 2.8 8.7 1.6 4c-.3-1 .3-2.1 1.4-2.5z" fill="var(--accent)"/>
        <path d="M9.5 1.5a5 5 0 0 1 5 5M9.5 3.8a2.7 2.7 0 0 1 2.7 2.7" fill="none" stroke="var(--accent)" stroke-width="1.1" stroke-linecap="round"/>
      </svg>
      <span>+61 3 9000 4821</span>
    </div>
    <div class="contact-item email">
      <svg width="17" height="17" viewBox="0 0 17 17" aria-hidden="true">
        <circle cx="8.5" cy="8.5" r="3" fill="none" stroke="var(--accent)" stroke-width="2"/>
        <path d="M11.5 6v3.6c0 1.4 2.8 1.4 3.3-.6A6.8 6.8 0 1 0 12 15" fill="none" stroke="var(--accent)" stroke-width="2" stroke-linecap="round"/>
      </svg>
      <span>info@brenmoors.com.au</span>
    </div>
    <div class="contact-item web">
      <svg width="17" height="17" viewBox="0 0 17 17" aria-hidden="true">
        <g fill="none" stroke="var(--accent)" stroke-width="1.1">
          <circle cx="8.5" cy="8.5" r="7.8"/>
          <ellipse cx="8.5" cy="8.5" rx="3.4" ry="7.8"/>
          <path d="M8.5 0.7v15.6M0.7 8.5h15.6M2 4.5h13M2 12.5h13"/>
        </g>
      </svg>
      <span>www.brenmoorsaccountants.com.au</span>
    </div>
  </header>

  <footer>
    <div class="est">EST. 1985</div>
    <div class="member-badge" role="img" aria-label="Professional membership badge"></div>
    <div class="registration-badge" role="img" aria-label="Tax practitioner registration badge"></div>
    <div class="tax-agent">Tax agent<br>40617283</div>
  </footer>
</div>
</body>
</html>
```